Start-up company developing economical and ecological hydrogen peroxide generator needs an attractiv

We need a powerpoint design for a start-up company based in Montreal called Verolune currently seeking to raise funds from investors. We develop an electrochemical hydrogen peroxide generator based on new generation catalysts.

These generators allow industrial users of hydrogen peroxide to generate it onsite economically and ecologically, as opposed to buying it from the major suppliers who make it large production plants using more polluting methods and need to transport it to customers over long distances.

We would like to see designs that have a cleantech technology and green chemistry feel. Colors that evoke a sense of environmental sustainability are desired.

The final design should communicate technological innovation that makes the world a cleaner and healthier place to live.

Target Market(s)

Industrial users or producers of of hydrogen peroxide

Industry/Entity Type

It Company

Font styles to use
Sans Serif

Colors
0255a3
3276b5
85acd3
9bcb3b
add136
e3eebf

Requirements
Must have
• Clean, attractive, professional and advanced technology look.
• Our slogan is: Catalyst for innovation
Nice to have
• The cover page should have our logo and our slogan. It should also have some graphics that pertain to technology and green chemistry. The perception that one should have when looking at it is that the company is developing a clean chemical manufacturing technology that is more environmentally friendly.
• Each other template page should have our logo discretely included in it.
• Other than the cover page, the template pages should not be too crowded with design elements. There should be lots of clear space to add material.
• I have uploaded some inspirational images that can be used to help come up with some designs.

```html
<!DOCTYPE html>
<html lang="en">
<head>
<meta charset="utf-8">
<title>Verolune – Presentation Template</title>
<link rel="stylesheet" href="https://fonts.googleapis.com/css2?family=Questrial&family=Open+Sans:ital,wght@0,400;0,700;1,400&display=swap">
<style>
  :root {
    --stage: #000000;
    --slide-white: #ffffff;
    --slide-tint: #f4f7ee;
    --brand-blue: #0255a3;
    --brand-blue-mid: #3276b5;
    --brand-blue-soft: #85acd3;
    --leaf-green: #9bcb3b;
    --lime-green: #add136;
    --mint-pale: #e3eebf;
    --ink: #2a2a2a;
    --body-grey: #6b6b6b;
  }
  * { margin: 0; padding: 0; box-sizing: border-box; }
  html, body {
    width: 1200px; height: 909px; overflow: hidden;
    background: var(--stage);
  }
  .sheet { position: relative; width: 1200px; height: 909px; }

  .slide {
    position: absolute; width: 565px; height: 424px;
    background: var(--slide-white); overflow: hidden;
  }
  .slide--cover       { left: 20px;  top: 17px;  background: var(--slide-tint); }
  .slide--section     { left: 615px; top: 17px; }
  .slide--content     { left: 21px;  top: 466px; }
  .slide--section-alt { left: 615px; top: 468px; }

  .artwork { position: absolute; left: 0; top: 0; width: 420px; height: 400px; }
  .artwork--cover {
    background:
      radial-gradient(ellipse 300px 260px at 8% 62%, rgba(255,255,255,0.95) 0%, rgba(173,209,54,0.55) 22%, rgba(173,209,54,0) 60%),
      radial-gradient(ellipse 380px 380px at 0% 45%, var(--brand-blue-mid) 0%, var(--brand-blue-soft) 45%, rgba(133,172,211,0.35) 75%, rgba(244,247,238,0) 100%);
  }
  .artwork--soft {
    background: radial-gradient(ellipse 330px 330px at 22% 50%, #e6ecd6 0%, #f1f5e6 50%, rgba(255,255,255,0) 100%);
  }

  .footer-rule {
    position: absolute; left: 0; right: 0; bottom: 20px;
    height: 3px; background: var(--leaf-green);
  }
  .footer-band {
    position: absolute; left: 0; right: 0; bottom: 0; height: 18px;
    background: linear-gradient(90deg, var(--brand-blue), var(--brand-blue-mid));
  }
  .page-number {
    position: absolute; right: 5px; bottom: 2px;
    font: 700 9px/14px "Open Sans", sans-serif; color: #fff;
  }

  .wordmark {
    position: absolute;
    font: 400 36px/1 "Questrial", sans-serif;
    color: var(--ink); letter-spacing: 0.5px; white-space: nowrap;
  }
  .slogan {
    position: absolute;
    font: italic 400 17px/1 "Questrial", "Open Sans", sans-serif;
    color: var(--ink); white-space: nowrap;
  }
  .slide--cover .wordmark { right: 16px; top: 313px; }
  .slide--cover .slogan   { right: 14px; top: 375px; }
  .slide--section .wordmark, .slide--section-alt .wordmark { right: 18px; top: 307px; }
  .slide--section .slogan,   .slide--section-alt .slogan   { right: 18px; top: 373px; }

  .section-title {
    position: absolute; left: 366px; top: 108px;
    font: 400 25px/1 "Questrial", sans-serif; color: var(--brand-blue);
    white-space: nowrap;
  }

  .header-shape { position: absolute; left: 0; top: 0; width: 565px; height: 50px; }
  .project-title {
    position: absolute; left: 13px; top: 8px;
    font: 700 20px/1.2 "Open Sans", sans-serif; color: #fff;
  }
  .slide--content .wordmark { right: 8px; top: 29px; font-size: 27px; }

  .column { position: absolute; top: 83px; width: 240px; }
  .column--left  { left: 26px; }
  .column--right { left: 295px; }
  .column h2 {
    font: 700 12.5px/1.3 "Open Sans", sans-serif; color: var(--brand-blue);
    margin-bottom: 3px;
  }
  .column p {
    font: 400 9.8px/15.5px "Open Sans", sans-serif; color: var(--body-grey);
    margin-bottom: 22px;
  }
</style>
</head>
<body>
<main class="sheet">

  <section class="slide slide--cover">
    <div class="artwork artwork--cover" role="img" aria-label="Glowing blue and green molecular structure of connected spheres"></div>
    <div class="wordmark">Verolune</div>
    <div class="slogan">Catalyst for innovation</div>
    <div class="footer-rule"></div>
    <div class="footer-band"></div>
  </section>

  <section class="slide slide--section">
    <div class="artwork artwork--soft" role="img" aria-label="Faint molecular structure over a hexagon grid"></div>
    <div class="section-title">Content Here</div>
    <div class="wordmark">Verolune</div>
    <div class="slogan">Catalyst for innovation</div>
    <div class="footer-rule"></div>
    <div class="footer-band"></div>
  </section>

  <section class="slide slide--content">
    <svg class="header-shape" viewBox="0 0 565 50" aria-hidden="true">
      <defs>
        <linearGradient id="headerBlue" x1="0" x2="1">
          <stop offset="0" stop-color="#0255a3"/>
          <stop offset="1" stop-color="#3276b5"/>
        </linearGradient>
      </defs>
      <path d="M0 0 H565 V13 H445 C420 13 410 40 370 43 H0 Z" fill="url(#headerBlue)"/>
      <path d="M0 46 H372 C414 43 422 17 447 17 H565" fill="none" stroke="#9bcb3b" stroke-width="2.5"/>
    </svg>
    <h1 class="project-title">Project Title Here</h1>
    <div class="wordmark">Verolune</div>

    <div class="column column--left">
      <h2>Lorem ipsum dolor sit</h2>
      <p>Lorem ipsum dolor sit&nbsp; Lorem ipsum dolor sit Lorem ipsum dolor sit&nbsp; Lorem ipsum dolor sit Lorem ipsum dolor sit&nbsp; Lorem ipsum dolor sit Lorem ipsum dolor sit Lorem ipsum dolor sit Lorem ipsum dolor sit&nbsp; Lorem ipsum dolor sit Lorem ipsum dolor sit&nbsp; Lorem ipsum dolor sit Lorem ipsum dolor sit&nbsp; Lorem ipsum dolor sit Lorem ipsum dolor sit</p>
      <p>Lorem ipsum dolor sit&nbsp; Lorem ipsum dolor sit Lorem ipsum dolor sit&nbsp; Lorem ipsum dolor sit Lorem ipsum dolor sit&nbsp; Lorem ipsum dolor sit Lorem ipsum dolor sit Lorem ipsum dolor sit Lorem ipsum dolor sit&nbsp; Lorem ipsum dolor sit Lorem ipsum dolor sit&nbsp; Lorem ipsum dolor sit Lorem ipsum dolor sit&nbsp; Lorem ipsum dolor sit Lorem ipsum dolor sit</p>
    </div>
    <div class="column column--right">
      <h2>Lorem ipsum dolor sit</h2>
      <p>Lorem ipsum dolor sit&nbsp; Lorem ipsum dolor sit Lorem ipsum dolor sit&nbsp; Lorem ipsum dolor sit Lorem ipsum dolor sit&nbsp; Lorem ipsum dolor sit Lorem ipsum dolor sit Lorem ipsum dolor sit Lorem ipsum dolor sit&nbsp; Lorem ipsum dolor sit Lorem ipsum dolor sit&nbsp; Lorem ipsum dolor sit Lorem ipsum dolor sit&nbsp; Lorem ipsum dolor sit Lorem ipsum dolor sit</p>
      <p>Lorem ipsum dolor sit&nbsp; Lorem ipsum dolor sit Lorem ipsum dolor sit&nbsp; Lorem ipsum dolor sit Lorem ipsum dolor sit&nbsp; Lorem ipsum dolor sit Lorem ipsum dolor sit Lorem ipsum dolor sit Lorem ipsum dolor sit&nbsp; Lorem ipsum dolor sit Lorem ipsum dolor sit&nbsp; Lorem ipsum dolor sit Lorem ipsum dolor sit&nbsp; Lorem ipsum dolor sit Lorem ipsum dolor sit</p>
    </div>

    <div class="footer-rule"></div>
    <div class="footer-band"><span class="page-number">Page : 01</span></div>
  </section>

  <section class="slide slide--section-alt">
    <div class="artwork artwork--soft" role="img" aria-label="Faint molecular structure over a hexagon grid"></div>
    <div class="section-title">Content Here</div>
    <div class="wordmark">Verolune</div>
    <div class="slogan">Catalyst for innovation</div>
    <div class="footer-rule"></div>
    <div class="footer-band"></div>
  </section>

</main>
</body>
</html>
```